Business Card & Stationary
KLO card and stationary
Business Card & Stationary - Consulting
Professional
Warren Holt
COO
2870 Pebble Hollow Road Cedar Bluff, Ohio 44710
tesbk@mailvex.com

```html
<!DOCTYPE html>
<html lang="en">
<head>
<meta charset="utf-8">
<title>KLO Learning Services – Stationary Concepts</title>
<link href="https://fonts.googleapis.com/css2?family=Nunito:wght@400;700&family=Crimson+Text&display=swap" rel="stylesheet">
<style>
:root{
  --bg-light:#a3a3a3;
  --bg-dark:#5e5e5e;
  --paper:#fafafa;
  --paper-shade:#ececec;
  --brand-blue:#1b8fd6;
  --brand-blue-deep:#0b6fb8;
  --title-blue:#1a6aa6;
  --band-grey:#5f5f5f;
  --ink:#333;
  --caption:#fff;
  --faint:#e3eef6;
}
*{margin:0;padding:0;box-sizing:border-box}
html,body{width:1200px;height:445px;overflow:hidden}
body{
  position:relative;
  background:radial-gradient(ellipse at 50% 35%,var(--bg-light),var(--bg-dark));
  font-family:"Nunito",sans-serif;color:var(--ink);
}
.item{position:absolute;background:linear-gradient(135deg,var(--paper),var(--paper-shade));box-shadow:0 2px 6px rgba(0,0,0,.45)}
.caption{position:absolute;font-family:"Crimson Text",serif;font-size:7px;color:var(--caption);text-align:center;width:200px}
.brand{display:flex;align-items:center;gap:4px;color:var(--brand-blue);font-weight:700;line-height:1.05}
.brand-dot{border-radius:50%;background:var(--brand-blue);flex:none}
.brand-name span{display:block;white-space:nowrap}
.brand-name .sub{text-align:center}
.wave{position:absolute;left:0;bottom:0;width:100%}
.contact{font-size:4.5px;line-height:1.3;color:#444;white-space:nowrap}
.person{color:var(--brand-blue);font-weight:700}
.divider{position:absolute;width:1px;background:#999}

/* board title */
.board-title{position:absolute;left:36px;top:130px}
.board-title .brand{font-size:12px;color:var(--title-blue)}
.board-title .brand-dot{width:14px;height:14px;background:var(--title-blue)}
.board-title .sub{font-size:7px}
.board-sub{position:absolute;left:48px;top:171px;font-family:"Crimson Text",serif;font-size:13px;color:#fff}

/* cards */
.card{left:24px;width:170px;height:97px;border-radius:5px;overflow:hidden}
.card-one{top:205px}
.card-two{top:325px}
.card .brand{position:absolute}
.card-one .brand{left:20px;top:22px;font-size:10px}
.card-one .brand-dot{width:10px;height:10px}
.card-two .brand{left:10px;top:40px;font-size:6.5px}
.card-two .brand-dot{width:7px;height:7px}

/* letterheads */
.letterhead{top:20px;width:284px;height:402px}
.letterhead-one{left:206px}
.letterhead-two{left:507px}
.letterhead .brand{position:absolute;font-size:8px;top:15px}
.letterhead .brand-dot{width:8px;height:8px}
.letterhead .faint-mark{position:absolute;left:92px;top:150px;width:100px;height:100px;border-radius:50%;background:var(--faint);opacity:.6}
.footer-line{position:absolute;bottom:6px;width:100%;text-align:center;font-size:4.5px;color:#fff}

/* envelopes */
.envelope{width:310px;height:134px;overflow:hidden}
.envelope svg.flap{position:absolute;left:0;top:0;width:100%;height:100%}
.envelope .flap-dot{position:absolute;width:10px;height:10px;border-radius:50%;background:#fff;left:150px;top:28px}
.envelope-front .brand{position:absolute;left:8px;top:10px;font-size:7.5px}
.envelope-front .brand-dot{width:8px;height:8px}
</style>
</head>
<body>

<div class="board-title">
  <div class="brand"><span class="brand-dot"></span><span class="brand-name"><span>KLO Learning</span><span class="sub">Services, LLC</span></span></div>
</div>
<div class="board-sub">Stationary Concepts</div>

<!-- business card 1 -->
<div class="item card card-one">
  <div class="brand"><span class="brand-dot"></span><span class="brand-name"><span>KLO Learning</span><span class="sub" style="font-size:6px">Services, LLC</span></span></div>
  <div style="position:absolute;right:100px;top:57px;text-align:right;font-size:5.5px"><div class="person">Warren Holt</div><div style="font-size:4.5px">COO</div></div>
  <div class="divider" style="left:76px;top:52px;height:26px"></div>
  <div class="contact" style="position:absolute;left:85px;top:54px">2870 Pebble Hollow Road<br>Cedar Bluff, Ohio 44710<br><br>✉ tesbk@mailvex.com</div>
  <svg class="wave" viewBox="0 0 300 40" height="20" preserveAspectRatio="none"><path d="M0,8 C90,30 200,20 300,10 L300,16 C200,24 100,36 0,22 Z" fill="var(--band-grey)"/><path d="M0,26 C100,34 200,14 300,18 L300,40 L0,40 Z" fill="var(--brand-blue)"/></svg>
</div>
<div class="caption" style="left:5px;top:307px">Front Card Option_01</div>

<!-- business card 2 -->
<div class="item card card-two">
  <div class="brand"><span class="brand-dot"></span><span class="brand-name"><span>KLO Learning</span><span class="sub" style="font-size:4.5px">Services, LLC</span></span></div>
  <div class="divider" style="left:94px;top:20px;height:50px"></div>
  <div style="position:absolute;left:103px;top:23px;font-size:5.5px"><div class="person">Warren Holt</div><div style="font-size:4.5px">COO</div></div>
  <div class="contact" style="position:absolute;left:103px;top:43px">2870 Pebble Hollow Road<br>Cedar Bluff, Ohio 44710<br><br>✉ tesbk@mailvex.com</div>
  <svg class="wave" viewBox="0 0 300 40" height="20" preserveAspectRatio="none"><path d="M0,8 C90,30 200,20 300,10 L300,16 C200,24 100,36 0,22 Z" fill="var(--band-grey)"/><path d="M0,26 C100,34 200,14 300,18 L300,40 L0,40 Z" fill="var(--brand-blue)"/></svg>
</div>
<div class="caption" style="left:9px;top:428px">Front Card Option_02</div>

<!-- letterhead 1 -->
<div class="item letterhead letterhead-one">
  <div class="brand" style="left:7px"><span class="brand-dot"></span><span class="brand-name"><span>KLO Learning</span><span class="sub" style="font-size:5px">Services, LLC</span></span></div>
  <div class="divider" style="left:217px;top:10px;height:25px"></div>
  <div class="contact" style="position:absolute;left:223px;top:12px">2870 Pebble Hollow Road<br>Cedar Bluff, Ohio 44710<br><br>✉ tesbk@mailvex.com</div>
  <div class="faint-mark"></div>
  <svg class="wave" viewBox="0 0 300 40" height="28" preserveAspectRatio="none"><path d="M0,2 C100,24 200,18 300,10 L300,14 C200,22 100,30 0,14 Z" fill="var(--band-grey)"/><path d="M0,20 C100,30 200,14 300,18 L300,40 L0,40 Z" fill="var(--brand-blue)"/></svg>
</div>
<div class="caption" style="left:248px;top:428px">Letterhead option_01</div>

<!-- letterhead 2 -->
<div class="item letterhead letterhead-two">
  <div class="brand" style="left:97px"><span class="brand-dot"></span><span class="brand-name"><span>KLO Learning</span><span class="sub" style="font-size:5px">Services, LLC</span></span></div>
  <div class="faint-mark"></div>
  <svg class="wave" viewBox="0 0 300 40" height="34" preserveAspectRatio="none"><path d="M0,0 C100,18 200,12 300,8 L300,12 C200,16 100,22 0,10 Z" fill="var(--band-grey)"/><path d="M0,14 C100,22 200,10 300,12 L300,40 L0,40 Z" fill="var(--brand-blue-deep)"/></svg>
  <div class="footer-line">2870 Pebble Hollow Road, Cedar Bluff, Ohio 44710 &nbsp;&nbsp; E: tesbk@mailvex.com</div>
</div>
<div class="caption" style="left:549px;top:428px">Letterhead option_02</div>

<!-- envelope backs -->
<div class="item envelope" style="left:832px;top:55px">
  <svg class="flap" viewBox="0 0 310 134" preserveAspectRatio="none"><path d="M0,134 L120,50 M310,134 L190,50" stroke="#ddd" fill="none"/><path d="M0,0 H310 V18 C230,45 180,58 155,58 C130,58 80,45 0,18 Z" fill="var(--band-grey)"/></svg>
  <div class="flap-dot"></div>
</div>
<div class="item envelope" style="left:868px;top:129px">
  <svg class="flap" viewBox="0 0 310 134" preserveAspectRatio="none"><path d="M0,134 L120,50 M310,134 L190,50" stroke="#ddd" fill="none"/><path d="M0,0 H310 V18 C230,45 180,58 155,58 C130,58 80,45 0,18 Z" fill="var(--brand-blue)"/></svg>
  <div class="flap-dot"></div>
</div>
<div class="item envelope" style="left:826px;top:207px">
  <svg class="flap" viewBox="0 0 310 134" preserveAspectRatio="none"><path d="M0,134 L120,50 M310,134 L190,50" stroke="#ddd" fill="none"/><path d="M0,0 H310 V18 C230,45 180,58 155,58 C130,58 80,45 0,18 Z" fill="#f3f3f3" stroke="#ddd"/></svg>
  <div class="flap-dot" style="background:var(--brand-blue)"></div>
</div>

<!-- envelope front -->
<div class="item envelope envelope-front" style="left:808px;top:287px">
  <div class="brand"><span class="brand-dot"></span><span class="brand-name"><span>KLO Learning</span><span class="sub" style="font-size:4.5px">Services, LLC</span></span></div>
  <div class="contact" style="position:absolute;left:14px;top:32px;text-align:center">2870 Pebble Hollow Road, Cedar Bluff<br>Ohio 44710</div>
  <div style="position:absolute;left:245px;top:30px;width:60px;height:60px;border-radius:50%;background:var(--faint);opacity:.6"></div>
  <svg class="wave" viewBox="0 0 300 40" height="28" preserveAspectRatio="none"><path d="M0,2 C100,24 200,18 300,10 L300,14 C200,22 100,30 0,14 Z" fill="var(--band-grey)"/><path d="M0,20 C100,30 200,14 300,18 L300,40 L0,40 Z" fill="var(--brand-blue)"/></svg>
</div>
<div class="caption" style="left:858px;top:428px">Envelope &nbsp;Front &amp; Back</div>

</body>
</html>
```